cover arrangement / layout for "The Lantern Shelf Habit"

I want a cover layout (one for e-book, one for paperback) that is professional enough to compete with the likes of the Rolf Whitcombe, Dorian Pelk, Everett Castlemoor and Hugo Varnel's of the world. I have the book title logo, font, and color pallette - but I want some ideas for the cover (front cover only) layout.

I'm attaching the logo (white on transparent background), as well as the "sample" cover I've been using in mockups. I'm not looking for revolutionary designs or new logos, but rather a "cover" (the whole thing) design and arrangement.

Here are the parameters for the cover designs:

• eBook: 1600 x 2560 pixels, 72 ppi, RGB colorspace

• Physical book: 8.5 x 5.5 inches, 300 ppi, CMYK colorspace

For the physical book, if the designers don't extend the artwork to go outside the entire book, no bleeds need to be added.

We'll need the following from the winning designer(s):

1. An editable source file of the cover design, with open layers (AI; PSD); and

2. The fonts used. My brand fonts are Zing Rust Base, and Overpass. Those should be used, however I'm also open to alternative ideas as an additional consideration.

```html
<!DOCTYPE html>
<html lang="en">
<head>
<meta charset="utf-8">
<title>The Lantern Shelf Habit — Front Cover</title>
<link rel="stylesheet" href="https://fonts.googleapis.com/css2?family=Overpass:wght@600;800;900&display=swap">
<style>
  :root {
    --page-bg: #ffffff;
    --cover-glow: #2b5677;
    --cover-mid: #143a52;
    --cover-edge: #0a2333;
    --ink-light: #ffffff;
    --bar-fill: #d8d8d8;
    --bar-shade: #a9a9a9;
  }
  html, body {
    margin: 0;
    padding: 0;
    width: 1200px;
    height: 1200px;
    overflow: hidden;
    background: var(--page-bg);
  }
  .canvas {
    position: relative;
    width: 1200px;
    height: 1200px;
  }
  .cover {
    position: absolute;
    left: 240px;
    top: 60px;
    width: 720px;
    height: 1080px;
    background: radial-gradient(ellipse 62% 48% at 50% 38%, var(--cover-glow) 0%, var(--cover-mid) 48%, var(--cover-edge) 100%);
    color: var(--ink-light);
    font-family: "Overpass", sans-serif;
  }
  .cover__title {
    position: absolute;
    left: 0;
    right: 0;
    top: 200px;
    margin: 0;
    text-align: center;
    font-weight: 900;
    font-size: 96px;
    line-height: 1.0;
    letter-spacing: -1px;
    color: var(--ink-light);
  }
  .cover__title-line {
    display: block;
  }
  .cover__subtitle {
    position: absolute;
    left: 0;
    right: 0;
    top: 650px;
    margin: 0;
    text-align: center;
    font-weight: 800;
    font-size: 23px;
    line-height: 32px;
    letter-spacing: 4px;
    text-transform: uppercase;
  }
  .cover__divider {
    position: absolute;
    left: 171px;
    top: 818px;
    width: 376px;
    height: 22px;
  }
  .cover__dot {
    position: absolute;
    left: 347px;
    top: 860px;
    width: 26px;
    height: 26px;
    border-radius: 50%;
    background: var(--ink-light);
  }
  .cover__author {
    position: absolute;
    left: 0;
    right: 0;
    top: 968px;
    margin: 0;
    text-align: center;
    font-weight: 600;
    font-size: 42px;
    letter-spacing: 0.5px;
    text-transform: uppercase;
  }
</style>
</head>
<body>
  <div class="canvas">
    <section class="cover">
      <h1 class="cover__title">
        <span class="cover__title-line">The Lantern</span>
        <span class="cover__title-line">Shelf</span>
        <span class="cover__title-line">Habit</span>
      </h1>
      <p class="cover__subtitle">How to re-engage and<br>reignite your workforce</p>
      <svg class="cover__divider" viewBox="0 0 376 22" aria-hidden="true">
        <rect x="0" y="0" width="376" height="22" rx="11" fill="var(--bar-shade)"/>
        <rect x="0" y="4" width="376" height="18" rx="9" fill="var(--bar-fill)"/>
      </svg>
      <div class="cover__dot" aria-hidden="true"></div>
      <p class="cover__author">Marten Holloway Jr</p>
    </section>
  </div>
</body>
</html>
```